Business Card Design needed for logo design project

Our company needs a Business Card Design. Please refer to our original project in the link above.

Industry/Entity Type

Business

```html
<!DOCTYPE html>
<html lang="en">
<head>
<meta charset="utf-8">
<title>Vellora Business Card</title>
<link href="https://fonts.googleapis.com/css2?family=Bebas+Neue&family=Quicksand:wght@400&family=Roboto:wght@400&display=swap" rel="stylesheet">
<style>
  :root {
    --backdrop: #efe9e2;
    --card: #515151;
    --rule: #d6d6d6;
    --ink: #ffffff;
    --ink-soft: #c4c4c4;
    --label: #4a4a4a;
  }
  * { margin: 0; padding: 0; box-sizing: border-box; }
  html, body { width: 1200px; height: 835px; overflow: hidden; }
  body {
    position: relative;
    background: var(--backdrop);
    font-family: "Roboto", Arial, sans-serif;
  }
  .card {
    position: absolute;
    width: 538px;
    height: 321px;
    background: var(--card);
    box-shadow: 0 6px 18px rgba(0,0,0,0.18);
  }
  .card--front { left: 131px; top: 78px; }
  .card--back { left: 565px; top: 431px; }

  .side-label {
    position: absolute;
    font-size: 35px;
    color: var(--label);
    transform: translateX(-50%);
  }
  .side-label--front { left: 304px; top: 406px; }
  .side-label--back { left: 858px; top: 768px; }

  /* Front */
  .brand-rule {
    position: absolute;
    top: 162px;
    height: 3px;
    background: var(--rule);
  }
  .brand-rule--left { left: 0; width: 178px; }
  .brand-rule--right { left: 362px; width: 176px; }
  .brand-name {
    position: absolute;
    left: 184px;
    width: 172px;
    top: 118px;
    text-align: center;
    font-family: "Quicksand", Arial, sans-serif;
    font-size: 58px;
    line-height: 1;
    color: var(--ink);
    letter-spacing: 1px;
  }
  .brand-url {
    position: absolute;
    right: 183px;
    top: 187px;
    font-size: 14px;
    color: var(--ink-soft);
  }

  /* Back */
  .accent-rule {
    position: absolute;
    left: 52px;
    width: 3px;
    background: var(--rule);
  }
  .accent-rule--top { top: 0; height: 128px; }
  .accent-rule--bottom { top: 256px; height: 65px; }
  .person-name {
    position: absolute;
    left: 51px;
    top: 138px;
    font-family: "Bebas Neue", Arial, sans-serif;
    font-size: 25px;
    color: var(--ink);
    letter-spacing: 0.3px;
  }
  .person-title {
    position: absolute;
    left: 51px;
    top: 168px;
    font-size: 15.5px;
    color: var(--ink-soft);
  }
  .contact {
    position: absolute;
    display: flex;
    align-items: center;
    gap: 7px;
    font-size: 16px;
    color: var(--ink);
  }
  .contact svg { width: 21px; height: 21px; flex: none; }
  .contact--phone { left: 51px; top: 202px; }
  .contact--email { left: 51px; top: 227px; }
  .contact--social-a { left: 266px; top: 202px; }
  .contact--social-b { left: 266px; top: 227px; }
</style>
</head>
<body>

  <section class="card card--front">
    <div class="brand-rule brand-rule--left"></div>
    <div class="brand-name">vellora</div>
    <div class="brand-rule brand-rule--right"></div>
    <div class="brand-url">www.vellora.com</div>
  </section>
  <div class="side-label side-label--front">Front Side</div>

  <section class="card card--back">
    <div class="accent-rule accent-rule--top"></div>
    <div class="person-name">Person Name</div>
    <div class="person-title">Managing Director</div>

    <div class="contact contact--phone">
      <svg viewBox="0 0 22 22" aria-hidden="true">
        <circle cx="11" cy="11" r="10" fill="none" stroke="#fff" stroke-width="1.6"/>
        <path d="M7.5 6c.6-.5 1.3-.4 1.6.2l.9 1.7c.2.5 0 1-.4 1.3l-.6.4c.5 1.3 1.5 2.3 2.8 2.9l.4-.6c.3-.4.8-.6 1.3-.4l1.7.9c.6.3.7 1 .2 1.6l-.8.8c-.7.6-1.8.7-3 .1-2.2-1.1-3.9-2.8-5-5-.6-1.2-.5-2.3.1-3z" fill="#fff"/>
      </svg>
      <span>555 210 4870</span>
    </div>
    <div class="contact contact--email">
      <svg viewBox="0 0 22 22" aria-hidden="true">
        <circle cx="11" cy="11" r="10" fill="none" stroke="#fff" stroke-width="1.6"/>
        <rect x="5.5" y="7.5" width="11" height="7.5" fill="none" stroke="#fff" stroke-width="1.3"/>
        <path d="M5.8 7.8 11 12l5.2-4.2" fill="none" stroke="#fff" stroke-width="1.3"/>
      </svg>
      <span>hello@vellora.com</span>
    </div>
    <div class="contact contact--social-a">
      <svg viewBox="0 0 22 22" aria-hidden="true">
        <circle cx="11" cy="11" r="10" fill="#fff"/>
      </svg>
      <span>linkup.net/name</span>
    </div>
    <div class="contact contact--social-b">
      <svg viewBox="0 0 22 22" aria-hidden="true">
        <circle cx="11" cy="11" r="10" fill="#fff"/>
      </svg>
      <span>chirpline.net/name</span>
    </div>

    <div class="accent-rule accent-rule--bottom"></div>
  </section>
  <div class="side-label side-label--back">Back Side</div>

</body>
</html>
```